Large multi-office optometry business opening a Dry Eye Spa and needs sign.

Business name/sign info: Brenwick Dry Eye Institute, (555) 362-4817
Backlit pole sign at office entrance on a very busy street
Sign dimensions: 53" tall x 136.5" wide
State of the art Dry Eye Spa for treatment of all forms of dry eye and ocular surface disease. Also, have aesthetics treatments (IPL, Low Level Light Treatment, etc.)

Target Market(s)

People who are suffering from: dryness, burning, foreign body sensation, itching, fluctuating vision, tired eyes, etc.

Industry/Entity Type

Optometry and aesthetics

Colors
0054AA
0677BA
7BADD7
CADEEF
E8F1F8

Requirements
Must have
• Business name, phone number, subliminal message of relief in a glance or short look.
Nice to have
• Cool, relief, soothing sense.
Should not have
• Too much information or too busy.

```html
<!DOCTYPE html>
<html lang="en">
<head>
<meta charset="utf-8">
<title>Brenwick Dry Eye Institute – Sign</title>
<link href="https://fonts.googleapis.com/css2?family=Poppins:wght@500;600;700&family=Roboto+Condensed:wght@700&display=swap" rel="stylesheet">
<style>
  :root {
    --navy: #213c8e;
    --sky: #29a6df;
    --brand-blue: #0677ba;
    --deep-blue: #0054aa;
    --tagline: #1b6cb5;
    --band-light: #2aaae2;
    --sign-bg: #f4f5f8;
    --page-bg: #e8f1f8;
    --white: #ffffff;
  }
  * { margin: 0; padding: 0; box-sizing: border-box; }
  html, body {
    width: 1200px; height: 929px; overflow: hidden;
    background: var(--page-bg);
  }
  .sign {
    position: absolute; left: 40px; top: 245px;
    width: 1120px; height: 440px;
    background: var(--sign-bg);
    overflow: hidden;
    font-family: "Poppins", sans-serif;
  }
  .sign-shapes { position: absolute; inset: 0; }
  .business-name {
    position: absolute; left: 21px; top: 10px;
    line-height: 66px;
    font-size: 68px;
  }
  .business-name span { display: block; white-space: nowrap; }
  .name-place { color: var(--navy); font-weight: 700; letter-spacing: 1px; }
  .name-focus { color: var(--sky); font-weight: 700; }
  .name-type { color: var(--navy); font-weight: 500; font-size: 64px; letter-spacing: 0.5px; }
  .divider {
    position: absolute; left: 21px; top: 233px;
    width: 348px; height: 5px; background: var(--navy);
  }
  .tagline {
    position: absolute; left: 21px; top: 258px;
    width: 400px;
    font-size: 16.5px; line-height: 23px; font-weight: 500;
    color: var(--tagline);
  }
  .phone {
    position: absolute; left: 21px; top: 358px; height: 59px;
    display: flex; align-items: center; gap: 20px;
    font-family: "Roboto Condensed", sans-serif;
    font-weight: 700; font-size: 42px; color: var(--white);
  }
  .phone svg { width: 32px; height: 32px; }
</style>
</head>
<body>
  <div class="sign">
    <svg class="sign-shapes" viewBox="0 0 1120 440" width="1120" height="440" aria-hidden="false">
      <defs>
        <linearGradient id="spa-photo-tone" x1="0" y1="1" x2="1" y2="0">
          <stop offset="0" stop-color="#e9dccd"/>
          <stop offset="0.45" stop-color="#e4c3a6"/>
          <stop offset="0.7" stop-color="#b99067"/>
          <stop offset="1" stop-color="#2f5ea6"/>
        </linearGradient>
      </defs>
      <path class="phone-band" d="M0 358 L612 358 L636 417 L0 417 Z" fill="var(--brand-blue)"/>
      <path class="eye-arc" d="M812 0 C650 40 475 140 391 222 C475 310 650 405 800 440 L768 440 C625 400 495 310 425 222 C495 140 625 48 778 0 Z" fill="var(--band-light)"/>
      <path class="spa-photo" role="img" aria-label="Photo of a relaxed client receiving a soothing temple massage at the dry eye spa" d="M1120 0 L826 0 C685 44 545 132 452 222 C545 318 685 404 826 440 L1120 440 Z" fill="url(#spa-photo-tone)"/>
    </svg>

    <h1 class="business-name">
      <span class="name-place">BRENWICK</span>
      <span class="name-focus">DRY EYE</span>
      <span class="name-type">INSTITUTE</span>
    </h1>
    <div class="divider"></div>
    <p class="tagline">State of the art Dry Eye Spa for treatment<br>of all forms of dry eye and ocular<br>surface disease.</p>
    <div class="phone">
      <svg viewBox="0 0 24 24" aria-hidden="true"><path fill="#ffffff" d="M6.6 10.8c1.4 2.8 3.8 5.1 6.6 6.6l2.2-2.2c.3-.3.7-.4 1-.2 1.1.4 2.3.6 3.6.6.6 0 1 .4 1 1V20c0 .6-.4 1-1 1C10.6 21 3 13.4 3 4c0-.6.4-1 1-1h3.5c.6 0 1 .4 1 1 0 1.3.2 2.5.6 3.6.1.3 0 .7-.2 1L6.6 10.8z"/></svg>
      <span class="phone-number">(555) 362-4817</span>
    </div>
  </div>
</body>
</html>
```